Wexley Malt Keller Beer Bottle Label #1

A beer bottle label is required for WMK's first beer that will go on sale later this year.
It is hoped that an on-going relationship will be formed with the successful designer.
Designs for glasses, packaging, t-shirts etc will also be required later this year.
Designs should reflect the local origin of the brewery and project an image of tradition and quality.
Designs should be simple, clean, classic and classy.
Designs should not be loud, bright, crazy or busy.
Design should include an element that can be used as brewery logo.
'Malt Keller' to be prominent, 'Wexley' to be discreet.
Name of first beer to be Wexil-Dunkel - label shall be easily adapted for different beers e.g. Wexil-Mirbt.
Deliverables include a smaller text only label for back of the bottle.

***I also need a logo that goes with my label design. So whoever submitted a logo that I like will be selected as the 2nd place winner.

Please refer to the attachment on this brief.

Requirements
Must have
• See uploaded design brief.
Nice to have
Should not have

```html
<!DOCTYPE html>
<html lang="en">
<head>
<meta charset="utf-8">
<title>Wexley Malt Keller – Wexil Dunkel label</title>
<link href="https://fonts.googleapis.com/css2?family=Comfortaa:wght@300&family=Kaushan+Script&family=Prata&family=Raleway:wght@300;400&display=swap" rel="stylesheet">
<style>
  :root{
    --backdrop:#e8e7e2;
    --ink:#151413;
    --cream:#f7f3ea;
    --copper:#c99460;
    --slate:#6e6b64;
    --stone:#a19e97;
    --straw:#e3c27c;
    --olive-gold:#a48a22;
    --gold:#c9962e;
    --claret:#8b1f27;
    --label-grey:#5d5b57;
  }
  *{margin:0;padding:0;box-sizing:border-box}
  html,body{width:1200px;height:796px;overflow:hidden;background:var(--backdrop)}
  .canvas{position:relative;width:1200px;height:796px;background:var(--backdrop);font-family:"Prata",serif;color:var(--ink)}

  .label{position:absolute;top:362px;width:166px;height:290px;background:var(--cream);border:5px solid var(--copper)}
  .label--slate{left:100px}
  .label--straw{left:318px;border-color:var(--stone)}
  .label__band{position:absolute;left:0;right:0;top:0;height:112px;background:var(--slate)}
  .label--straw .label__band{background:var(--straw)}
  .label__rules{position:absolute;left:0;right:0;top:112px;height:14px;
    background:repeating-linear-gradient(to bottom,var(--copper) 0 2px,transparent 2px 5px)}
  .label--straw .label__rules{background:repeating-linear-gradient(to bottom,var(--stone) 0 2px,transparent 2px 5px)}
  .label__wheat{position:absolute;top:14px;width:30px;height:70px;border-radius:50% 50% 40% 40%;background:var(--gold);opacity:.8}
  .label__wheat--left{left:14px}
  .label__wheat--right{right:14px}
  .label__mark{position:absolute;left:50%;top:8px;transform:translateX(-50%);width:82px;height:128px;
    background:var(--cream);border:3px solid var(--stone);border-radius:41px 41px 40px 40px;
    display:flex;flex-direction:column;align-items:center;justify-content:center;gap:6px}
  .label__mark-dot{width:20px;height:20px;border-radius:50%;background:var(--claret)}
  .label__mark-name{font-family:"Raleway",sans-serif;font-weight:400;font-size:15px;letter-spacing:1px;color:var(--claret)}
  .label__beer{position:absolute;left:0;right:0;top:138px;text-align:center}
  .label__beer-name{display:block;font-family:"Comfortaa",sans-serif;font-weight:300;font-size:29px;line-height:30px;color:var(--olive-gold)}
  .label__beer-style{display:block;font-family:"Kaushan Script",cursive;font-size:36px;line-height:34px;color:var(--gold);margin-top:-4px}
  .label__brewery{position:absolute;left:0;right:0;top:220px;text-align:center;font-family:"Raleway",sans-serif;font-weight:300;color:var(--label-grey)}
  .label__brewery-name{display:block;font-size:16px;line-height:18px}
  .label__brewery-town{display:block;font-size:12px;line-height:14px}
  .label__facts{position:absolute;left:8px;right:8px;bottom:6px;display:flex;justify-content:space-between;font-family:"Prata",serif;font-size:7.5px;color:var(--label-grey)}

  .brand{position:absolute;left:720px;top:60px;width:352px;text-align:center}
  .brand__mark{display:flex;flex-direction:column;align-items:center;justify-content:center;height:470px;gap:24px}
  .brand__square{width:120px;height:120px;background:var(--claret)}
  .brand__name{font-family:"Prata",serif;font-size:34px;line-height:42px;color:var(--claret)}
  .brand__tagline{position:absolute;left:640px;width:512px;text-align:center}
  .brand__headline{top:560px;font-size:58px;line-height:70px}
  .brand__strap{top:650px;font-size:31px;line-height:40px}
</style>
</head>
<body>
<main class="canvas">
  <section class="label label--slate">
    <div class="label__band"></div>
    <div class="label__rules"></div>
    <div class="label__wheat label__wheat--left" role="img" aria-label="Wheat ear ornament"></div>
    <div class="label__wheat label__wheat--right" role="img" aria-label="Wheat ear ornament"></div>
    <div class="label__mark"><span class="label__mark-dot"></span><span class="label__mark-name">WMK</span></div>
    <h2 class="label__beer"><span class="label__beer-name">Wexil</span><span class="label__beer-style">Dunkel</span></h2>
    <p class="label__brewery"><span class="label__brewery-name">MALT KELLER</span><span class="label__brewery-town">Wexley</span></p>
    <p class="label__facts"><span>ABV 4.6%</span><span>2.3 Units</span><span>500ml</span></p>
  </section>

  <section class="label label--straw">
    <div class="label__band"></div>
    <div class="label__rules"></div>
    <div class="label__wheat label__wheat--left" role="img" aria-label="Wheat ear ornament"></div>
    <div class="label__wheat label__wheat--right" role="img" aria-label="Wheat ear ornament"></div>
    <div class="label__mark"><span class="label__mark-dot"></span><span class="label__mark-name">WMK</span></div>
    <h2 class="label__beer"><span class="label__beer-name">Wexil</span><span class="label__beer-style">Dunkel</span></h2>
    <p class="label__brewery"><span class="label__brewery-name">MALT KELLER</span><span class="label__brewery-town">Wexley</span></p>
    <p class="label__facts"><span>ABV 4.6%</span><span>2.3 Units</span><span>500ml</span></p>
  </section>

  <div class="brand">
    <div class="brand__mark">
      <span class="brand__square"></span>
      <span class="brand__name">Wexley Malt Keller</span>
    </div>
  </div>
  <h1 class="brand__tagline brand__headline">Wexil beer.</h1>
  <p class="brand__tagline brand__strap">Miles away from ordinary</p>
</main>
</body>
</html>
```